42 on Birch Apartment Mailer to Competition

I need a postcard mailer designed that will be promoting a new apartment building in downtown Rochester NY. The postcards are being mailed to other apartment communities the we are in direct competition with. I have enclosed a bunch of info to guide you.

Target Market(s)

Other communities in the market

Industry/Entity Type

Property Management

Requirements
Must have
• Exterior rendering, features. Fit standard postcard, colors similar to enclosed, grey, white coral
Nice to have
• Interior Pictures

```html
<!DOCTYPE html>
<html lang="en">
<head>
<meta charset="utf-8">
<title>42 on Birch – Postcard Mailer</title>
<link rel="stylesheet" href="https://fonts.googleapis.com/css2?family=PT+Sans+Narrow:wght@400;700&display=swap">
<style>
  :root {
    --backdrop: #fbe7e5;
    --card: #ffffff;
    --maroon: #4a1515;
    --maroon-deep: #3a0f10;
    --coral: #e2322b;
    --ink: #2a1a1a;
    --paper-text: #ffffff;
    --photo-sky: #8fa3b4;
    --photo-warm: #b9a48f;
    --photo-shade: #5b5e5a;
    --interior-light: #b7a796;
    --interior-dark: #4d4540;
  }
  * { box-sizing: border-box; margin: 0; padding: 0; }
  html, body {
    width: 1200px; height: 1035px; overflow: hidden;
    background: var(--backdrop);
    font-family: "PT Sans Narrow", "Arial Narrow", sans-serif;
  }
  .postcard {
    position: absolute;
    background: var(--card);
    border-radius: 14px; overflow: hidden;
    box-shadow: 0 6px 18px rgba(90, 40, 40, 0.18);
  }
  .postcard-art { position: absolute; inset: 0; }

  /* Front */
  .postcard-front { left: 30px; top: 90px; width: 560px; height: 860px; }
  .brand {
    position: absolute; display: flex; align-items: center; justify-content: center; gap: 7px;
    color: var(--maroon); font-weight: 700; text-transform: uppercase; letter-spacing: 0.5px;
    white-space: nowrap;
  }
  .brand-mark { background: var(--maroon); flex: none; }
  .postcard-front .brand { left: 6px; top: 155px; width: 160px; font-size: 24px; }
  .postcard-front .brand-mark { width: 12px; height: 12px; }
  .section { position: absolute; text-align: center; }
  .section-title {
    color: var(--coral); font-weight: 700; font-size: 28px;
    text-transform: uppercase; line-height: 1.05; margin-bottom: 4px;
  }
  .section-line { font-size: 14px; line-height: 1.5; white-space: nowrap; }
  .sep { color: var(--coral); padding: 0 3px; }
  .community { left: 20px; top: 410px; width: 520px; color: var(--ink); }
  .home { left: 20px; top: 612px; width: 520px; color: var(--paper-text); }
  .plans { left: 210px; top: 780px; width: 340px; color: var(--ink); }

  /* Back */
  .postcard-back { left: 610px; top: 90px; width: 570px; height: 380px; }
  .postcard-back .brand { left: 8px; top: 34px; width: 150px; font-size: 17px; }
  .postcard-back .brand-mark { width: 9px; height: 9px; }
  .contact { position: absolute; left: 22px; top: 190px; width: 270px; color: var(--paper-text); }
  .contact-call { font-size: 27px; font-weight: 700; line-height: 1.05; text-transform: uppercase; }
  .contact-phone { color: var(--coral); font-size: 31px; font-weight: 700; line-height: 1.15; margin-top: 2px; }
  .contact-line { font-size: 16px; line-height: 1.25; text-transform: uppercase; }
  .contact-social { font-size: 12px; line-height: 1.3; margin-top: 6px; }
</style>
</head>
<body>
  <article class="postcard postcard-front">
    <svg class="postcard-art" width="560" height="860" viewBox="0 0 560 860">
      <defs>
        <linearGradient id="exterior-tone" x1="0" y1="0" x2="0.4" y2="1">
          <stop offset="0" stop-color="var(--photo-sky)"/>
          <stop offset="0.55" stop-color="var(--photo-warm)"/>
          <stop offset="1" stop-color="var(--photo-shade)"/>
        </linearGradient>
      </defs>
      <path class="exterior-rendering" role="img" aria-label="Exterior rendering of the glass apartment building at dusk on a downtown street"
            d="M0,0 H560 V330 Q280,360 0,400 Z" fill="url(#exterior-tone)"/>
      <path d="M0,400 Q280,360 560,330" fill="none" stroke="var(--coral)" stroke-width="4"/>
      <circle class="brand-badge" cx="30" cy="170" r="145" fill="var(--card)" stroke="var(--maroon)" stroke-width="3"/>
      <circle cx="30" cy="170" r="139" fill="none" stroke="var(--coral)" stroke-width="3"/>
      <path class="feature-band" d="M0,600 Q300,545 560,530 V745 Q300,760 150,860 H0 Z" fill="var(--maroon-deep)"/>
      <path d="M0,600 Q300,545 560,530" fill="none" stroke="var(--coral)" stroke-width="4"/>
      <path d="M560,745 Q300,760 150,860" fill="none" stroke="var(--coral)" stroke-width="4"/>
    </svg>

    <div class="brand"><span class="brand-mark"></span>42 on Birch</div>

    <section class="section community">
      <h2 class="section-title">Community Features</h2>
      <p class="section-line">Rooftop patio<span class="sep">|</span>24 Hour Fitness<span class="sep">|</span>5x10 Storage Unit<span class="sep">|</span>High Speed Internet and cable Included</p>
      <p class="section-line">Heat and A/C Included<span class="sep">|</span>Parking Available, One Spot Included</p>
      <p class="section-line">Modern Security with Controlled Access and Key Fobs<span class="sep">|</span>Amazing Views<span class="sep">|</span>Den Available</p>
      <p class="section-line">24 Hour Maintenance</p>
    </section>

    <section class="section home">
      <h2 class="section-title">Home Features</h2>
      <p class="section-line">Floor to Ceiling Operable Windows<span class="sep">|</span>W/D In Unit<span class="sep">|</span>LED Lighting<span class="sep">|</span>Hardwood Flooring</p>
      <p class="section-line">Automatic Window Treatments<span class="sep">|</span>Granite Countertops<span class="sep">|</span>Undermount Sinks</p>
      <p class="section-line">Tile backsplash<span class="sep">|</span>Walk-in Closets Available<span class="sep">|</span>Open Floor Plans</p>
      <p class="section-line">Contemporary Cabinetry and Fixtures</p>
    </section>

    <section class="section plans">
      <h2 class="section-title">Floor Plans</h2>
      <p class="section-line">1 Bedroom, 1 Bedroom with Den, and 2 Bedroom 2 Bath Available</p>
      <p class="section-line">$1400 to $3300<span class="sep">|</span>775 to 1677 sq. ft.</p>
    </section>
  </article>

  <article class="postcard postcard-back">
    <svg class="postcard-art" width="570" height="380" viewBox="0 0 570 380">
      <defs>
        <linearGradient id="kitchen-tone" x1="0" y1="0" x2="1" y2="1">
          <stop offset="0" stop-color="var(--interior-light)"/>
          <stop offset="1" stop-color="var(--interior-dark)"/>
        </linearGradient>
        <linearGradient id="living-tone" x1="0" y1="0" x2="1" y2="1">
          <stop offset="0" stop-color="#a8987f"/>
          <stop offset="1" stop-color="#6d6257"/>
        </linearGradient>
      </defs>
      <path class="contact-panel" d="M0,0 H300 Q350,190 300,380 H0 Z" fill="var(--maroon)"/>
      <path d="M300,0 Q350,190 300,380" fill="none" stroke="var(--coral)" stroke-width="4"/>
      <path class="brand-tab" d="M0,14 H130 A34,34 0 0 1 130,82 H0 Z" fill="var(--card)" stroke="var(--coral)" stroke-width="3"/>
      <rect class="interior-photo" role="img" aria-label="Interior photo of the apartment kitchen with island and stools"
            x="10" y="94" width="160" height="80" fill="url(#kitchen-tone)"/>
      <path class="interior-photo" role="img" aria-label="Interior photo of an apartment living space"
            d="M176,94 H322 Q326,134 326,174 H176 Z" fill="url(#living-tone)"/>
      <line x1="0" y1="180" x2="327" y2="180" stroke="var(--coral)" stroke-width="3"/>
    </svg>

    <div class="brand"><span class="brand-mark"></span>42 on Birch</div>

    <section class="contact">
      <p class="contact-call">Call Today<br>For Information</p>
      <p class="contact-phone">585.555.0142</p>
      <p class="contact-line">Leasing@42onbirch.com</p>
      <p class="contact-line">www.42onbirch.com</p>
      <p class="contact-social">Follow us online<br>@42onbirch</p>
    </section>
  </article>
</body>
</html>
```